Copper Ridge Golf Circle Chart

I would like some type of design that can then be used on our website, like a png. or .jpeg or vector format. We want a circle/flow chart that describes our golf coaching process and has our logo faded in the background. attached is a rough draft to give you a general idea..something I created in word document but would like a much better version and attached is our logo. Our colors are red, black, and grey. The design does not necessarily have to have all of the bullet points..

Target Market(s)

Golfers, junior high golfers, high school golfers, adult golfers

Font styles to use
Sans Serif

Colors
ec1f27
f04a50
f59296
fbd4d5
aaaaaa
cbcbcb
1b1b1b
474747

Requirements
Nice to have
• Our colors are red, black, and grey, do not have to use all 3 in one design. Also The design does not necessarily have to have all of the bullet points.

```html
<!DOCTYPE html>
<html lang="en">
<head>
<meta charset="utf-8">
<title>Copper Ridge Golf Coaching Process</title>
<link rel="stylesheet" href="https://fonts.googleapis.com/css2?family=Noto+Serif:wght@400;600&family=Oswald:wght@700&display=swap">
<style>
  :root {
    --red: #ec1f27;
    --ink: #1b1b1b;
    --slate: #474747;
    --paper: #fafafa;
    --label-text: #f4f4f4;
  }
  html, body { margin: 0; padding: 0; overflow: hidden; }
  body { background: var(--paper); }
  .canvas {
    position: relative;
    width: 1200px;
    height: 993px;
    overflow: hidden;
    background: var(--paper);
    font-family: "Noto Serif", Georgia, serif;
  }
  .step-label {
    position: absolute;
    background: var(--slate);
    color: var(--label-text);
    border-radius: 9px;
    font-size: 26px;
    line-height: 30px;
    padding: 3px 16px;
    box-sizing: border-box;
    white-space: nowrap;
  }
  .step-label.left { text-align: left; }
  .step-label.right { text-align: right; }
  .step-label.two-line { padding-top: 2px; }
  .process-wheel { position: absolute; inset: 0; }
  .segment-title {
    font-family: "Oswald", "Arial Narrow", sans-serif;
    font-weight: 700;
    fill: var(--ink);
  }
  .brand-name {
    font-family: "Noto Serif", Georgia, serif;
    font-weight: 600;
    fill: var(--red);
    font-size: 34px;
  }
</style>
</head>
<body>
<div class="canvas">
  <!-- evaluation details -->
  <div class="step-label left" style="left:134px; top:270px; width:350px; height:36px;">Video Swing Analysis</div>
  <div class="step-label left" style="left:160px; top:328px; width:260px; height:37px;">Putting Reports</div>
  <div class="step-label left" style="left:122px; top:387px; width:250px; height:37px;">Develope a Plan</div>

  <!-- coaching details -->
  <div class="step-label right" style="left:690px; top:261px; width:388px; height:37px;">Tour Quality Technology</div>
  <div class="step-label left two-line" style="left:790px; top:320px; width:232px; height:60px; padding-left:18px;">Visualization &amp;<br>&nbsp;&nbsp;Feedback</div>
  <div class="step-label left two-line" style="left:832px; top:402px; width:230px; height:61px; padding-left:18px;">Understand<br>&nbsp;Inconsitencies</div>

  <!-- practice details -->
  <div class="step-label left two-line" style="left:808px; top:573px; width:195px; height:62px; padding-left:30px;">24/7 Access<br>to Practice</div>
  <div class="step-label left two-line" style="left:720px; top:656px; width:261px; height:62px; padding-left:40px;">&nbsp;&nbsp;&nbsp;Practice with<br>a Purpose</div>

  <!-- measure progress details -->
  <div class="step-label right two-line" style="left:163px; top:614px; width:260px; height:64px; padding-right:32px;">Track Progress<br>with Data</div>

  <svg class="process-wheel" width="1200" height="993" viewBox="0 0 1200 993" aria-label="Coaching process wheel">
    <defs>
      <path id="arc-evaluation" d="M 436 496 A 160 160 0 0 1 596 336"/>
      <path id="arc-coaching" d="M 596 336 A 160 160 0 0 1 756 496"/>
      <path id="arc-practice" d="M 596 734 A 238 238 0 0 0 834 496"/>
      <path id="arc-measure" d="M 400 496 A 196 196 0 0 0 596 692"/>
      <path id="arc-progress" d="M 358 496 A 238 238 0 0 0 596 734"/>
      <marker id="flow-head" markerWidth="8" markerHeight="8" refX="6" refY="4" orient="auto" markerUnits="userSpaceOnUse">
        <path d="M0,0 L8,4 L0,8 Z" fill="var(--slate)"/>
      </marker>
    </defs>

    <circle cx="596" cy="496" r="253" fill="var(--red)"/>
    <rect x="593" y="240" width="5" height="512" fill="var(--paper)"/>
    <rect x="340" y="494" width="512" height="5" fill="var(--paper)"/>
    <circle cx="596" cy="496" r="150" fill="var(--paper)"/>

    <g fill="none" stroke="var(--slate)" stroke-width="3" marker-end="url(#flow-head)">
      <path d="M 450 488 A 146 146 0 0 1 588 350"/>
      <path d="M 604 350 A 146 146 0 0 1 742 488"/>
      <path d="M 742 504 A 146 146 0 0 1 604 642"/>
      <path d="M 588 642 A 146 146 0 0 1 450 504"/>
    </g>

    <text class="segment-title" font-size="78">
      <textPath href="#arc-evaluation" startOffset="50%" text-anchor="middle" textLength="232" lengthAdjust="spacingAndGlyphs">EVALUATION</textPath>
    </text>
    <text class="segment-title" font-size="78">
      <textPath href="#arc-coaching" startOffset="50%" text-anchor="middle" textLength="222" lengthAdjust="spacingAndGlyphs">COACHING</textPath>
    </text>
    <text class="segment-title" font-size="72">
      <textPath href="#arc-practice" startOffset="50%" text-anchor="middle" textLength="225" lengthAdjust="spacingAndGlyphs">PRACTICE</textPath>
    </text>
    <text class="segment-title" font-size="46">
      <textPath href="#arc-measure" startOffset="50%" text-anchor="middle" textLength="180" lengthAdjust="spacingAndGlyphs">MEASURE</textPath>
    </text>
    <text class="segment-title" font-size="46">
      <textPath href="#arc-progress" startOffset="50%" text-anchor="middle" textLength="222" lengthAdjust="spacingAndGlyphs">PROGRESS</textPath>
    </text>

    <text class="brand-name" x="596" y="468" text-anchor="middle">Copper</text>
    <text class="brand-name" x="596" y="510" text-anchor="middle">Ridge</text>
    <text class="brand-name" x="596" y="552" text-anchor="middle">Golf</text>
  </svg>
</div>
</body>
</html>
```